Corvane Holdings needs a business card

I would like the card to be simple but modern and elegant.
I like black and white.
or black and gold.
we are a private finance lender and also are involved in property and property developments.

please look at the business card photos i provided i would like C.H only one one side and all the other details on the other side use fonts that tie in with my theme.

Industry/Entity Type

Finance

Contact Information for Business Card

Corvane Holdings (C.H) Elliot Marbury M: 0413586102 E: elliotmar@examplemail.net

Font styles to use
Other font styles liked:
• Use fonts that would reflect our business

Colors
000000
ffffff

Requirements
Must have
• one side of details
• other side has either C.H or Corvane Holdings like in the photos provided

```html
<!DOCTYPE html>
<html lang="en">
<head>
<meta charset="utf-8">
<title>Corvane Holdings — Business Card</title>
<link rel="stylesheet" href="https://fonts.googleapis.com/css2?family=Cormorant+Garamond:wght@500&family=Crimson+Text&family=Source+Sans+3:wght@400&display=swap">
<style>
  :root {
    --page: #ffffff;
    --card: #000000;
    --ink: #ffffff;
    --note: #111111;
    --varnish: #5a5a5a;
    --varnish-dark: #3a3a3a;
    --gold-light: #f3d99a;
    --gold: #c8933f;
    --gold-dark: #8a5a1c;
  }
  * { margin: 0; padding: 0; box-sizing: border-box; }
  html, body { width: 1200px; height: 639px; overflow: hidden; background: var(--page); }
  .stage { position: relative; width: 1200px; height: 639px; background: var(--page); }

  .print-note {
    position: absolute; left: 44px; top: 34px;
    font: 400 19px/1 "Source Sans 3", sans-serif; color: var(--note);
  }
  .callout {
    position: absolute; left: 21px; top: 342px;
    font: 400 14px/1 "Source Sans 3", sans-serif; color: var(--note);
  }
  .callout-arrow { position: absolute; left: 162px; top: 344px; z-index: 2; }

  .card {
    position: absolute; width: 278px; height: 502px; background: var(--card);
    box-shadow: 0 4px 14px rgba(0,0,0,0.45);
    overflow: hidden;
  }
  .card--back { left: 170px; top: 106px; }
  .card--silver { left: 527px; top: 110px; }
  .card--gold { left: 874px; top: 110px; }

  .monogram {
    position: absolute; left: 0; width: 100%; text-align: center;
    font: 500 112px/1 "Cormorant Garamond", serif; letter-spacing: 0;
  }
  .card--back .monogram {
    top: 166px; font-size: 124px;
    background: linear-gradient(180deg, var(--varnish) 0%, var(--varnish-dark) 100%);
    -webkit-background-clip: text; background-clip: text; color: transparent;
  }
  .card--silver .monogram, .card--gold .monogram { top: 118px; }
  .card--silver .monogram { color: var(--ink); }

  .rule { position: absolute; left: 42px; top: 247px; }

  .name {
    position: absolute; left: 0; top: 310px; width: 100%; text-align: center;
    font: 400 28px/1 "Crimson Text", serif; color: var(--ink);
  }
  .contact {
    position: absolute; display: flex; align-items: center; gap: 8px;
    font: 400 16px/1 "Crimson Text", serif; color: var(--ink);
  }
  .card--silver .contact--phone { left: 31px; top: 384px; }
  .card--silver .contact--mail { left: 31px; top: 403px; }
  .card--gold .contact--phone { left: 30px; top: 384px; gap: 14px; }
  .card--gold .contact--mail { left: 30px; top: 410px; gap: 14px; }

  .gold-text {
    background: linear-gradient(180deg, var(--gold-light) 0%, var(--gold) 55%, var(--gold-dark) 100%);
    -webkit-background-clip: text; background-clip: text; color: transparent;
  }
  .card--gold .contact span { color: var(--gold-light); }
</style>
</head>
<body>
<div class="stage">
  <p class="print-note">I advise paper «Velmora», it is very pleasant to the touch and It looks good selective varnishing and gold embossing</p>

  <p class="callout">Selective varnishing</p>
  <svg class="callout-arrow" width="96" height="12" viewBox="0 0 96 12" aria-hidden="true">
    <line x1="0" y1="6" x2="88" y2="6" stroke="#d9d9d9" stroke-width="1.2"/>
    <path d="M96 6 L86 2 L88 6 L86 10 Z" fill="#ffffff"/>
  </svg>

  <section class="card card--back" aria-label="Card back">
    <div class="monogram">C.H</div>
  </section>

  <section class="card card--silver" aria-label="Card front, white">
    <div class="monogram">C.H</div>
    <svg class="rule" width="195" height="6" viewBox="0 0 195 6" aria-hidden="true">
      <path d="M0 3 Q97 0 195 3 Q97 6 0 3 Z" fill="#ffffff"/>
    </svg>
    <div class="name">Elliot Marbury</div>
    <div class="contact contact--phone">
      <svg width="12" height="18" viewBox="0 0 12 18" aria-hidden="true">
        <rect x="1" y="1" width="10" height="16" rx="1.5" fill="none" stroke="#fff" stroke-width="1.4"/>
        <rect x="3" y="3" width="6" height="5" fill="#fff"/>
        <rect x="3" y="10" width="6" height="5" fill="#fff" opacity="0.8"/>
      </svg>
      <span>0413586102</span>
    </div>
    <div class="contact contact--mail">
      <svg width="16" height="11" viewBox="0 0 16 11" aria-hidden="true">
        <rect x="0.6" y="0.6" width="14.8" height="9.8" fill="#fff"/>
        <path d="M0.6 0.6 L8 6 L15.4 0.6" fill="none" stroke="#000" stroke-width="1"/>
      </svg>
      <span>elliotmar@examplemail.net</span>
    </div>
  </section>

  <section class="card card--gold" aria-label="Card front, gold">
    <svg width="0" height="0" aria-hidden="true">
      <defs>
        <linearGradient id="goldFill" x1="0" y1="0" x2="1" y2="1">
          <stop offset="0" stop-color="#f3d99a"/>
          <stop offset="0.55" stop-color="#c8933f"/>
          <stop offset="1" stop-color="#8a5a1c"/>
        </linearGradient>
      </defs>
    </svg>
    <div class="monogram gold-text">C.H</div>
    <svg class="rule" width="195" height="6" viewBox="0 0 195 6" aria-hidden="true">
      <path d="M0 3 Q97 0 195 3 Q97 6 0 3 Z" fill="url(#goldFill)"/>
    </svg>
    <div class="name gold-text">Elliot Marbury</div>
    <div class="contact contact--phone">
      <svg width="16" height="20" viewBox="0 0 16 20" aria-hidden="true">
        <path d="M4 1 L7 5 L5 7 Q6 12 10 15 L12 13 L15 17 L12 19 Q2 15 1 4 Z" fill="url(#goldFill)"/>
      </svg>
      <span>0413586102</span>
    </div>
    <div class="contact contact--mail">
      <svg width="22" height="14" viewBox="0 0 22 14" aria-hidden="true">
        <rect x="0" y="0" width="22" height="14" fill="url(#goldFill)"/>
        <path d="M0 0 L11 8 L22 0 M0 14 L8 6 M22 14 L14 6" fill="none" stroke="#000" stroke-width="1"/>
      </svg>
      <span>elliotmar@examplemail.net</span>
    </div>
  </section>
</div>
</body>
</html>
```